Business cards design on a high standard

We advise clients on insurance and financial matters, since these clients pay for our advice, the design should have a high standard. Our logo should be included. From the colors we are open for everything.

Colors

Designer to choose colors to be used in the design.

```html
<!DOCTYPE html>
<html lang="en">
<head>
<meta charset="utf-8">
<title>Halden Advisory – Business Card</title>
<link rel="stylesheet" href="https://fonts.googleapis.com/css2?family=Ubuntu:wght@400;500;700&display=swap">
<style>
  :root {
    --brand-red: #e31e24;
    --swoosh-grey: #a3a3a3;
    --card-white: #f7f8f8;
    --ink: #1f1f1f;
    --backdrop: #e3e4e6;
  }
  * { margin: 0; padding: 0; box-sizing: border-box; }
  html, body {
    width: 1200px;
    height: 545px;
    overflow: hidden;
    background: var(--backdrop);
    font-family: "Ubuntu", sans-serif;
  }
  .stage {
    position: relative;
    width: 1306px;
    height: 593px;
    transform: scale(0.9188);
    transform-origin: 0 0;
  }
  .card {
    position: absolute;
    top: 170px;
    width: 562px;
    height: 336px;
    background: var(--card-white);
    overflow: hidden;
  }
  .card--front { left: 65px; }
  .card--back { left: 679px; }
  .card__art {
    position: absolute;
    inset: 0;
    width: 100%;
    height: 100%;
  }
  .art-red { fill: var(--brand-red); }
  .art-grey { fill: var(--swoosh-grey); }

  .holder-name {
    position: absolute;
    left: 49px;
    top: 45px;
    color: #fff;
    font-weight: 700;
    font-size: 21px;
    letter-spacing: 0.5px;
  }
  .wordmark {
    position: absolute;
    color: var(--brand-red);
    font-weight: 700;
    line-height: 1;
    text-align: right;
  }
  .wordmark__name { display: block; font-size: 44px; letter-spacing: 2px; }
  .wordmark__line { display: block; font-size: 17px; letter-spacing: 5px; margin-top: 4px; }
  .card--front .wordmark { right: 50px; top: 110px; }
  .card--back .wordmark { left: 0; right: 0; top: 128px; text-align: center; }

  .address {
    position: absolute;
    left: 49px;
    top: 253px;
    font-size: 14.5px;
    line-height: 20px;
    color: var(--ink);
  }
  .contact {
    position: absolute;
    right: 50px;
    top: 213px;
    font-size: 14.5px;
    line-height: 20px;
    color: var(--ink);
    text-align: right;
  }
  .contact__web { color: var(--brand-red); font-weight: 700; }
</style>
</head>
<body>
<main class="stage">
  <section class="card card--front" aria-label="Business card front">
    <svg class="card__art" viewBox="0 0 562 336" aria-hidden="true">
      <path class="art-red" d="M0 0 H562 V62 C400 40 170 100 0 240 Z"/>
      <path class="art-grey" d="M0 244 C170 105 330 58 455 54 C330 68 165 135 0 264 Z"/>
    </svg>
    <p class="holder-name">YOUR NAME</p>
    <p class="wordmark"><span class="wordmark__name">HALDEN</span><span class="wordmark__line">ADVISORY</span></p>
    <p class="address">Your Adderess, City<br>State, ZIP&nbsp; 00000, Country</p>
    <p class="contact">
      Office: (000) 000-0000<br>
      Cell: (000) 000-0000<br>
      Mail: your@email.com<br>
      <span class="contact__web">www.yourwebsite.com</span>
    </p>
  </section>

  <section class="card card--back" aria-label="Business card back">
    <svg class="card__art" viewBox="0 0 562 336" aria-hidden="true">
      <path class="art-red" d="M0 0 H245 C130 40 45 140 0 252 Z"/>
      <path class="art-grey" d="M320 0 C170 30 55 130 22 240 C75 135 180 45 330 0 Z"/>
      <path class="art-red" d="M562 84 V336 H318 C440 300 530 200 562 84 Z"/>
      <path class="art-grey" d="M240 336 C380 305 500 230 540 125 C505 240 400 310 262 336 Z"/>
    </svg>
    <p class="wordmark"><span class="wordmark__name">HALDEN</span><span class="wordmark__line">ADVISORY</span></p>
  </section>
</main>
</body>
</html>
```